Red Gum Wrecking P/L business card

I already have a EPS logo design that I wish to use however, the company is a demolition company based on the Central Coast of NSW Australia. The company is called "Red Gum Wrecking P/L".

We offer demolition services such as Residential, Commercial, Civil, Asbestos removal, Excavation and Tree removal that are required to be displayed on the rear of the business card.

We currently have 4 personnel that require business cards with their specific contact details.

The logo is mid blue on a white background and the remainder is black text on a whiter card.

The eps logo supplied should only be displayed as a logo without the text.

Target Market(s)

People, governments, companies requiring demolition services on the east coast of NSW, specifically Central Coast, Sydney and Newcastle locations.

Industry/Entity Type

Business

Contact Information for Business Card

There are four cards required
First card:
Martin Elsby
Operations Director
Mobile No. 0462 815094
E: info@redgumwreck.com.au
www.redgumwreck.com.au
Second card:
Peter Halloran
Project Director
Company Mobile: 0462 815094
Personal Mobile: 0428 160 384
www.redgumwreck.com.au
Third card:
Simon Preddy
Project Director
Company Mobile: 0462 815 094
Personal Mobile: 0433 958217
www.redgumwreck.com.au
Fourth card:
Neil Brathwaite
General Manager
Personal Mobile: 0437 281609
www.redgumwreck.com.au

Font styles to use
Other font styles liked:
• Helvetica

Colors
33a6d7

Requirements
Must have
• The RGW logo (without the text of Red Gum Wrecking)
Horizontal layout with logo on top left hand corner
Services provision on the rear of the card
Nice to have
• Logo on top left corner
Text should be something like Helvetica
Should not have
• Do not include the text that is incorporated in the EPS file I sent ….just the logo

```html
<!DOCTYPE html>
<html lang="en">
<head>
<meta charset="utf-8">
<title>Red Gum Wrecking P/L – Business Card</title>
<link rel="stylesheet" href="https://fonts.googleapis.com/css2?family=Montserrat:wght@500&family=Open+Sans:ital,wght@0,400;0,600;1,400;1,700&display=swap">
<style>
  :root {
    --teal: #2eaac5;
    --card-white: #ffffff;
    --card-grey: #e4e6e8;
    --page-bg: #eef0f2;
    --text-white: #ffffff;
  }
  * { margin: 0; padding: 0; box-sizing: border-box; }
  html, body {
    width: 1200px; height: 900px; overflow: hidden;
    background: var(--page-bg);
  }
  .canvas { position: relative; width: 1200px; height: 900px; }

  .card {
    position: absolute;
    width: 640px; height: 366px;
    border-radius: 26px;
    overflow: hidden;
    background: radial-gradient(ellipse at 55% 40%, var(--card-white) 0%, #f4f5f6 55%, var(--card-grey) 100%);
    box-shadow: 0 8px 22px rgba(0,0,0,0.18);
  }
  .card--back  { left: 90px;  top: 60px; }
  .card--front { left: 470px; top: 474px; }

  .brand {
    position: absolute;
    display: flex; align-items: center; gap: 12px;
    font-family: "Montserrat", Helvetica, Arial, sans-serif;
    font-weight: 500;
    color: var(--teal);
    letter-spacing: 1px;
    white-space: nowrap;
  }
  .brand__dot {
    flex: none;
    width: 30px; height: 30px; border-radius: 50%;
    background: var(--teal);
  }
  .card--back .brand { left: 50%; top: 44%; transform: translate(-50%, -50%); font-size: 34px; }
  .card--back .brand__dot { width: 40px; height: 40px; }
  .card--front .brand { left: 48px; top: 46px; font-size: 26px; }

  .services {
    position: absolute; left: 0; right: 0; top: 232px;
    display: flex; justify-content: center; flex-wrap: wrap; gap: 6px 16px;
    padding: 0 60px;
    list-style: none;
    font-family: "Open Sans", Helvetica, Arial, sans-serif;
    font-size: 13px; font-weight: 600;
    letter-spacing: 0.5px;
    color: var(--teal);
  }
  .services li { white-space: nowrap; }

  .wave { position: absolute; inset: 0; width: 100%; height: 100%; }

  .holder {
    position: absolute; left: 34px; top: 276px;
    font-family: "Open Sans", Helvetica, Arial, sans-serif;
    color: var(--text-white);
    font-style: italic;
  }
  .holder__name  { font-weight: 700; font-size: 22px; line-height: 1.2; }
  .holder__title { font-weight: 400; font-size: 18px; line-height: 1.25; }

  .contacts {
    position: absolute; left: 426px; top: 230px;
    list-style: none;
    font-family: "Open Sans", Helvetica, Arial, sans-serif;
    font-size: 13px; color: var(--text-white);
  }
  .contacts li { display: flex; align-items: center; gap: 7px; margin-bottom: 6px; line-height: 1.3; white-space: nowrap; }
  .contacts svg { display: block; flex: none; width: 14px; height: 14px; }
</style>
</head>
<body>
<main class="canvas">

  <section class="card card--back" aria-label="Card back">
    <div class="brand"><span class="brand__dot"></span>Red Gum Wrecking</div>
    <ul class="services" aria-label="Services">
      <li>Residential</li>
      <li>Commercial</li>
      <li>Civil</li>
      <li>Asbestos Removal</li>
      <li>Excavation</li>
      <li>Tree Removal</li>
    </ul>
  </section>

  <section class="card card--front" aria-label="Card front">
    <svg class="wave" viewBox="0 0 640 366" preserveAspectRatio="none" aria-hidden="true">
      <path d="M0 206 Q300 290 610 122 Q320 268 0 220 Z" fill="var(--teal)"/>
      <path d="M0 238 Q330 300 640 118 L640 366 L0 366 Z" fill="var(--teal)"/>
    </svg>

    <div class="brand"><span class="brand__dot"></span>Red Gum Wrecking</div>

    <div class="holder">
      <p class="holder__name">Martin Elsby</p>
      <p class="holder__title">Operations Director</p>
    </div>

    <ul class="contacts">
      <li>
        <svg viewBox="0 0 14 14"><circle cx="7" cy="7" r="7" fill="#fff"/><path d="M3.5 7.5 L7 4 L10.5 7.5 V10.5 H3.5 Z" fill="var(--teal)"/></svg>
        <span>Central Coast, NSW</span>
      </li>
      <li>
        <svg viewBox="0 0 14 14"><circle cx="7" cy="7" r="7" fill="#fff"/><rect x="5" y="3" width="4" height="8" rx="0.8" fill="var(--teal)"/></svg>
        <span>0462 815094</span>
      </li>
      <li>
        <svg viewBox="0 0 14 14"><circle cx="7" cy="7" r="7" fill="#fff"/><rect x="3.5" y="4.5" width="7" height="5" fill="var(--teal)"/><path d="M3.5 4.5 L7 7.3 L10.5 4.5" stroke="#fff" stroke-width="0.8" fill="none"/></svg>
        <span>info@redgumwreck.com.au</span>
      </li>
      <li>
        <svg viewBox="0 0 14 14"><circle cx="7" cy="7" r="7" fill="#fff"/><circle cx="7" cy="7" r="3.6" fill="none" stroke="var(--teal)" stroke-width="1"/><path d="M3.4 7 H10.6 M7 3.4 V10.6" stroke="var(--teal)" stroke-width="0.9"/></svg>
        <span>www.redgumwreck.com.au</span>
      </li>
    </ul>
  </section>

</main>
</body>
</html>
```